Wellspring Care Alliance Vonzo Ads

We want an ad created for the gay dating app vonzo. The size is 300x250. We want the ad to be sexy, with a shirtless man. We are advertising our free HIV and PrEP services. We are open to slogans about maybe "Bringing HIV and PrEP To You"
"Free PrEP and HIV Management"
Open to ideas.

We also offer through the Harborlight Support Fund
Copay Assistance, Insurance Premium Assistance, Free Medical Services, etc
Our website is wcanj.org

I do want the ad to have a Book Now Button

Gay sexually active males

```html
<!DOCTYPE html>
<html lang="en">
<head>
<meta charset="utf-8">
<title>Wellspring Care Alliance – Vonzo Ad</title>
<link rel="stylesheet" href="https://fonts.googleapis.com/css2?family=Poppins:wght@400;500;600;700&display=swap">
<style>
  :root {
    --stage: #e9e9e9;
    --card: #ffffff;
    --ink: #1f2430;
    --body-ink: #2b2f3a;
    --brand: #4a3fd4;
    --brand-dot: #8a3fe0;
    --check: #f0562f;
    --grad-blue: #1f6ff2;
    --grad-magenta: #d633d8;
    --grad-orange: #ff6a3d;
    --photo-light: #e8d6c8;
    --photo-mid: #b98a6c;
    --photo-dark: #7a5442;
  }
  * { margin: 0; padding: 0; box-sizing: border-box; }
  html, body { width: 1200px; height: 1026px; overflow: hidden; }
  body {
    background: var(--stage);
    font-family: "Poppins", Arial, sans-serif;
    position: relative;
  }
  .ad {
    position: absolute;
    left: 150px; top: 135px;
    width: 900px; height: 750px;
    background: var(--card);
    overflow: hidden;
  }
  .ad__photo {
    position: absolute; inset: 0;
    width: 900px; height: 750px;
  }
  .brand {
    position: absolute;
    left: 60px; top: 48px;
    display: flex; align-items: center; gap: 18px;
  }
  .brand__dot {
    width: 62px; height: 62px; border-radius: 50%;
    background: var(--brand-dot);
  }
  .brand__name {
    color: var(--brand);
    font-weight: 700;
    font-size: 27px;
    line-height: 32px;
    width: 230px;
  }
  .headline {
    position: absolute;
    left: 60px; top: 170px;
    color: var(--ink);
    font-weight: 700;
    font-size: 36px;
    line-height: 60px;
    text-transform: uppercase;
    width: 420px;
  }
  .benefits {
    position: absolute;
    left: 60px; top: 315px;
    list-style: none;
    display: flex; flex-direction: column; gap: 24px;
  }
  .benefits__item {
    display: flex; align-items: flex-start; gap: 24px;
    color: var(--body-ink);
    font-size: 27px; line-height: 36px;
    width: 390px;
  }
  .benefits__icon { flex: none; width: 27px; height: 27px; margin-top: 4px; }
  .book-btn {
    position: absolute;
    left: 60px; top: 609px;
    width: 264px; height: 72px;
    border-radius: 36px;
    background: linear-gradient(90deg, var(--grad-blue), var(--grad-magenta) 55%, var(--grad-orange));
    display: flex; align-items: center; justify-content: center; gap: 12px;
    color: #fff; font-weight: 700; font-size: 24px;
    text-decoration: none; letter-spacing: 0.5px;
  }
  .book-btn svg { width: 26px; height: 26px; }
</style>
</head>
<body>
  <div class="ad">
    <svg class="ad__photo" viewBox="0 0 900 750" role="img" aria-label="Photo of two shirtless men embracing on white bedding">
      <defs>
        <linearGradient id="photoTone" x1="0" y1="0" x2="1" y2="1">
          <stop offset="0" stop-color="var(--photo-light)"/>
          <stop offset="0.45" stop-color="var(--photo-mid)"/>
          <stop offset="1" stop-color="var(--photo-dark)"/>
        </linearGradient>
        <linearGradient id="edgeTone" x1="0" y1="0" x2="0" y2="1">
          <stop offset="0" stop-color="var(--grad-magenta)"/>
          <stop offset="0.5" stop-color="#8a3fe0"/>
          <stop offset="1" stop-color="var(--grad-blue)"/>
        </linearGradient>
      </defs>
      <path d="M560,0 C470,200 420,520 565,750 L900,750 L900,0 Z" fill="url(#photoTone)"/>
      <path d="M560,0 C470,200 420,520 565,750" fill="none" stroke="url(#edgeTone)" stroke-width="9"/>
    </svg>

    <div class="brand">
      <span class="brand__dot"></span>
      <span class="brand__name">Wellspring Care Alliance</span>
    </div>

    <h1 class="headline">Bringing HIV and PrEP to you</h1>

    <ul class="benefits">
      <li class="benefits__item">
        <svg class="benefits__icon" viewBox="0 0 24 24"><rect x="2" y="4" width="17" height="17" rx="2" fill="none" stroke="var(--check)" stroke-width="2.2"/><path d="M6 12l4 4 11-12" fill="none" stroke="var(--check)" stroke-width="2.6" stroke-linecap="round" stroke-linejoin="round"/></svg>
        <span>Harborlight Support Fund</span>
      </li>
      <li class="benefits__item">
        <svg class="benefits__icon" viewBox="0 0 24 24"><rect x="2" y="4" width="17" height="17" rx="2" fill="none" stroke="var(--check)" stroke-width="2.2"/><path d="M6 12l4 4 11-12" fill="none" stroke="var(--check)" stroke-width="2.6" stroke-linecap="round" stroke-linejoin="round"/></svg>
        <span>Copay Assistance</span>
      </li>
      <li class="benefits__item">
        <svg class="benefits__icon" viewBox="0 0 24 24"><rect x="2" y="4" width="17" height="17" rx="2" fill="none" stroke="var(--check)" stroke-width="2.2"/><path d="M6 12l4 4 11-12" fill="none" stroke="var(--check)" stroke-width="2.6" stroke-linecap="round" stroke-linejoin="round"/></svg>
        <span>Insurance Premium Assistance</span>
      </li>
      <li class="benefits__item">
        <svg class="benefits__icon" viewBox="0 0 24 24"><rect x="2" y="4" width="17" height="17" rx="2" fill="none" stroke="var(--check)" stroke-width="2.2"/><path d="M6 12l4 4 11-12" fill="none" stroke="var(--check)" stroke-width="2.6" stroke-linecap="round" stroke-linejoin="round"/></svg>
        <span>Free Medical Services</span>
      </li>
    </ul>

    <a class="book-btn" href="#">
      BOOK NOW
      <svg viewBox="0 0 24 24"><circle cx="12" cy="12" r="11" fill="#fff"/><path d="M8 12h8M13 8l4 4-4 4" fill="none" stroke="var(--grad-magenta)" stroke-width="2.6" stroke-linecap="round" stroke-linejoin="round"/></svg>
    </a>
  </div>
</body>
</html>
```